KAL stands for Kit and Lenora - teenager girls that will provide makeup and photography services for proms, weddings, graduations and other special events. The design should be bright and cheery and have the teenage audience it will be directed to in mind. I want the word "KAL" to be a part of the postcard and be essentially a logo by itself with the names somewhere under it.

Target Market(s)

Teenagers

Industry/Entity Type

Makeup

Requirements
Must have
• The Word "KAL" as the logo for the make up and photography services with the girls name in smaller font somewhere to identify what "KAL" stands for.
Nice to have
• I like circles and bright colors. I like tie dye too. There should be room to put a couple photos of their work on the postcard.
Should not have
• No address will be proved

```html
<!DOCTYPE html>
<html lang="en">
<head>
<meta charset="utf-8">
<title>KAL makeup and photography postcard</title>
<link rel="stylesheet" href="https://fonts.googleapis.com/css2?family=Lora:ital,wght@0,400;1,400&display=swap">
<style>
:root{
  --purple:#7d2f91;
  --purple-dark:#6a2480;
  --pink:#e0306e;
  --ink:#1d1d1d;
  --yellow:#f4ec2c;
  --photo-a:#7a6a62;
  --photo-b:#c9b2a4;
  --bg-top:#ffffff;
  --bg-bottom:#e4e4e4;
}
*{margin:0;padding:0;box-sizing:border-box}
html,body{width:1200px;height:1200px;overflow:hidden}
body{
  background:linear-gradient(180deg,var(--bg-top) 0%,var(--bg-bottom) 100%);
  font-family:"Lora",Georgia,serif;
  position:relative;
  color:var(--ink);
}
.card{position:absolute;background:#fff;overflow:hidden;box-shadow:3px 4px 8px rgba(0,0,0,.28)}
.card svg.shape{position:absolute;left:0;top:0}
.abs{position:absolute}

/* front */
.front{left:62px;top:31px;width:692px;height:536px}
.front .logo{left:16px;top:22px;font-size:68px;line-height:1;color:var(--purple);letter-spacing:2px}
.front .tagline{left:17px;top:107px;font-size:18.5px;font-style:italic;color:var(--purple)}
.front .intro{left:21px;top:151px;width:262px;font-size:15.3px;line-height:19.3px;font-style:italic}
.front .intro .names{color:var(--pink)}
.front .services-title{left:21px;top:248px;font-size:20px;font-style:italic;color:var(--purple)}
.services{left:22px;top:290px;list-style:none}
.services li{font-size:15.5px;font-style:italic;height:35px;display:flex;align-items:flex-start;gap:4px}
.services svg{margin-top:5px;flex:none}
.offer{left:246px;top:341px;width:156px;height:156px;border-radius:50%;background:var(--yellow);
  display:flex;flex-direction:column;align-items:center;justify-content:center;transform:rotate(-20deg);font-style:italic;text-align:center;line-height:1.1}
.offer .o1{font-size:19px}
.offer .o2{font-size:25px}
.offer .o3{font-size:14.5px;width:110px}
.appointment{right:27px;top:455px;text-align:right;color:#fff;font-style:italic}
.appointment .label{font-size:21px}
.appointment .phone{font-size:34px;margin-top:4px}

/* back */
.back{left:386px;top:606px;width:696px;height:537px}
.back .price-title{left:29px;top:27px;font-size:25px;font-style:italic;color:#fff}
.price-group{left:29px;color:#fff;font-style:italic}
.price-group h3{font-weight:400;font-size:19.5px;margin-bottom:12px}
.price-group p{font-size:15px;height:27.6px}
.hair{top:86px}
.photo{top:302px}
.back .note{left:15px;top:439px;width:262px;font-size:14px;line-height:17.3px;color:#fff;font-style:italic}
.sender{left:331px;top:44px}
.sender .name{font-size:21px;color:var(--purple)}
.sender .sub{font-size:10px;font-style:italic;margin-top:2px}
.sender .contact{font-size:10px;font-style:italic;margin-top:8px;line-height:16px}
.stamp{left:512px;top:44px;width:119px;height:118px;border:2px solid #111}
</style>
</head>
<body>

<section class="card front" aria-label="Postcard front">
  <svg class="shape" width="692" height="536" viewBox="0 0 692 536">
    <path d="M0,476 C140,520 270,500 420,445 C540,405 630,405 692,420 L692,536 L0,536 Z" fill="var(--purple)"/>
    <path d="M0,452 C140,505 270,488 420,432 C540,393 630,393 692,408" fill="none" stroke="var(--purple)" stroke-width="3"/>
    <path d="M0,466 C140,514 270,496 420,440 C540,400 630,400 692,414" fill="none" stroke="#fff" stroke-width="2"/>
    <circle cx="422" cy="170" r="134" fill="var(--purple)"/>
    <circle cx="428" cy="164" r="128" fill="var(--photo-a)" role="img" aria-label="Portrait photo of a bride with curly dark hair, veil and hair flower"/>
    <circle cx="575" cy="281" r="114" fill="var(--purple)"/>
    <circle cx="573" cy="281" r="108" fill="#fff"/>
    <circle cx="573" cy="281" r="104" fill="var(--photo-b)" role="img" aria-label="Portrait photo of a bride with styled hair and makeup"/>
  </svg>

  <div class="abs logo">KAL</div>
  <div class="abs tagline">makeup and photography</div>
  <p class="abs intro"><span class="names">Kit and Lenora</span> are freelance Hair, Make-up &amp; Photography, specializing in proms, weddings, graduations and other special events</p>
  <h2 class="abs services-title" style="font-weight:400">List Of Services We Offer</h2>
  <ul class="abs services">
    <li><svg width="10" height="9" viewBox="0 0 10 9"><path d="M1,5 L4,8 L9,1" fill="none" stroke="#1d1d1d" stroke-width="2"/></svg>Lorem ipsum dolor sit amet</li>
    <li><svg width="10" height="9" viewBox="0 0 10 9"><path d="M1,5 L4,8 L9,1" fill="none" stroke="#1d1d1d" stroke-width="2"/></svg>Consectetuer adipiscing elit</li>
    <li><svg width="10" height="9" viewBox="0 0 10 9"><path d="M1,5 L4,8 L9,1" fill="none" stroke="#1d1d1d" stroke-width="2"/></svg>Sed diam nonummy nibh</li>
    <li><svg width="10" height="9" viewBox="0 0 10 9"><path d="M1,5 L4,8 L9,1" fill="none" stroke="#1d1d1d" stroke-width="2"/></svg>Tncidunt ut laoreet</li>
    <li><svg width="10" height="9" viewBox="0 0 10 9"><path d="M1,5 L4,8 L9,1" fill="none" stroke="#1d1d1d" stroke-width="2"/></svg>Sliquam erat volutpat.</li>
  </ul>
  <div class="abs offer">
    <span class="o1">Special Offer</span>
    <span class="o2">Get $30 off</span>
    <span class="o3">some offer text goes here</span>
  </div>
  <div class="abs appointment">
    <div class="label">For Appointment Call</div>
    <div class="phone">555-014-2768</div>
  </div>
</section>

<section class="card back" aria-label="Postcard back">
  <svg class="shape" width="696" height="537" viewBox="0 0 696 537">
    <path d="M0,0 L268,0 C345,110 350,330 240,537 L0,537 Z" fill="var(--purple)"/>
    <path d="M277,0 C352,110 357,330 249,537" fill="none" stroke="var(--purple)" stroke-width="2"/>
  </svg>

  <h2 class="abs price-title" style="font-weight:400">Services Price List</h2>
  <div class="abs price-group hair">
    <h3>Hair and Beauty</h3>
    <p>Service..............................Cost</p>
    <p>Service..............................Cost</p>
    <p>Service..............................Cost</p>
    <p>Service..............................Cost</p>
    <p>Service..............................Cost</p>
    <p>Service..............................Cost</p>
  </div>
  <div class="abs price-group photo">
    <h3>Photography</h3>
    <p>1 Hour Photography................Cost</p>
    <p>2 Hour Photography................Cost</p>
    <p>3Hour Photography................Cost</p>
  </div>
  <p class="abs note">You will receive a minimum of 80 high resolution photos in digital Jpeg format for every hour of photography, beautifully presented on a USB stick</p>

  <div class="abs sender">
    <div class="name">Kit and Lenora</div>
    <div class="sub">makeup and photography services</div>
    <div class="contact">555-014-2768<br>KALmakeupandphoto@example.com</div>
  </div>
  <div class="abs stamp" aria-label="Stamp area"></div>
</section>

</body>
</html>
```